New Fernwick 4 Loop waste management business seeking web site

New project for business offering sustainable options within the waste industry.
Business called Fernwick 4 Loop
Targeting the consumer & industry professionals the web site needs to be able to accommodate both.
Needs to have a modern clean feel.
Logo being designed by another pro and will be completed early next week and will be submitted soon after to be incorporated into the web page
Links to another web page i like very much to take into consideration.

Target Market(s)

Industry professionals, consumers and producers of all waste, Food, constructruction, commercial, retail .. etc..

Industry/Entity Type

Waste Management

Coding

Coded - Design and coding required

Number of Pages Required

5+ page

Font styles to use
Serif
Script

Requirements
Must have
• Flexabilty, all pages as in examples
Nice to have
• Open to offers you guys and gals are the pro's

```html
<!DOCTYPE html>
<html lang="en">
<head>
<meta charset="utf-8">
<title>Fernwick 4 Loop — Recovery &amp; Recycling</title>
<link href="https://fonts.googleapis.com/css2?family=Raleway:wght@400;600;700;800&family=Open+Sans:ital,wght@0,400;0,600;0,700;1,400&display=swap" rel="stylesheet">
<style>
:root{
  --red:#a8070d;
  --green:#4f8a04;
  --dark:#3c3c3c;
  --text:#5a5a5a;
  --muted:#8a8a8a;
  --blue:#3c79b8;
  --rose:#c0585e;
  --gold:#d8a82f;
  --grey:#8f8f8f;
  --footer:#2e2e2e;
  --footer-bottom:#242424;
  --white:#ffffff;
}
*{margin:0;padding:0;box-sizing:border-box}
html,body{width:1200px;height:2791px;overflow:hidden;background:var(--white)}
body{position:relative;font-family:"Open Sans",Arial,sans-serif;color:var(--text)}
.abs{position:absolute}
.center{text-align:center;left:0;width:1200px}
h1,h2,h3{font-family:"Raleway",Arial,sans-serif}

/* hero */
.hero{position:absolute;left:0;top:0;width:1200px;height:587px;
  background:linear-gradient(180deg,#3b3d3f 0%,#55585a 35%,#6b6560 60%,#4a4440 100%)}
.hero::after{content:"";position:absolute;inset:0;background:rgba(0,0,0,.28)}
.brand{position:absolute;left:0;top:0;width:223px;height:93px;background:var(--white);z-index:2;
  display:flex;align-items:center;justify-content:center;gap:8px}
.brand-dot{width:14px;height:14px;border-radius:50%;background:var(--green)}
.brand-name{font-family:"Raleway",sans-serif;font-weight:700;color:var(--red);font-size:19px}
.menu-btn{position:absolute;left:223px;top:0;width:93px;height:93px;background:var(--red);z-index:2}
.menu-btn span{position:absolute;left:35px;width:24px;height:3px;background:var(--white)}
.hero-title{position:absolute;z-index:2;top:282px;font-weight:800;font-size:43px;color:var(--white)}
.hero-sub{position:absolute;z-index:2;top:336px;font-weight:700;font-size:28px;color:var(--white)}
.btn{position:absolute;z-index:2;height:54px;color:var(--white);font-size:13px;font-weight:600;
  display:flex;align-items:center;justify-content:center;text-transform:uppercase}
.dots{position:absolute;z-index:2;top:555px;left:577px;display:flex;gap:6px}
.dots i{width:6px;height:6px;border-radius:50%;background:rgba(255,255,255,.6)}
.dots i:first-child{background:rgba(255,255,255,.35)}

/* intro */
.intro-title{top:666px;font-size:45px;font-weight:700;color:var(--dark)}
.intro-sub{top:728px;font-size:25px;letter-spacing:7px;color:var(--dark);font-weight:400}
.intro-text{top:785px;left:150px;width:900px;font-size:11.5px;line-height:28px;color:var(--muted);text-align:center}
.section-title{font-size:29px;font-weight:600;color:var(--dark)}
.r{color:var(--red)}.g{color:var(--green)}

/* services */
.card{position:absolute;top:1007px;width:244px;height:238px}
.card-photo{height:178px}
.card-label{height:60px;color:var(--white);text-align:center;padding-top:12px}
.card-label b{display:block;font-size:11.5px;font-weight:700}
.card-label em{display:block;font-size:9.5px;margin-top:4px}

/* markets band */
.band{position:absolute;top:1328px;left:0;width:1200px;height:164px;background:var(--green)}
.band-line{position:absolute;top:40px;left:0;width:1200px;text-align:center;color:var(--white);font-size:16px}
.band-line strong{font-family:"Raleway",sans-serif;font-size:25px;font-weight:700;margin-right:6px}
.band-btn{position:absolute;left:500px;top:88px;width:201px;height:45px;border:1px solid var(--white);
  color:var(--white);font-size:13px;font-weight:600;display:flex;align-items:center;justify-content:center}

/* development */
.dev{position:absolute;top:1492px;left:0;width:1200px;height:508px;
  background:linear-gradient(180deg,#e4e4e4,#ececec 50%,#dedede)}
.dev-text{left:150px;width:900px;font-size:11.5px;line-height:27px;color:var(--muted);text-align:center}
.step-text{position:absolute;color:var(--white);font-size:11px;line-height:20px;width:178px}
.step-text b{display:block;font-size:13px;line-height:18px;margin-bottom:4px}

/* testimonials */
.quote{position:absolute;top:2210px;width:300px;font-style:italic;font-size:10.5px;line-height:21px;color:var(--text)}
.who{position:absolute;top:2300px;font-size:12px;font-weight:700;color:var(--green)}
.role{position:absolute;top:2322px;font-size:10.5px;font-style:italic;color:var(--muted)}
.mark{position:absolute;font-family:Georgia,serif;font-size:34px;color:#c9c9c9}

/* footer */
.footer{position:absolute;top:2460px;left:0;width:1200px;height:267px;background:var(--footer)}
.footer-bottom{position:absolute;top:2727px;left:0;width:1200px;height:64px;background:var(--footer-bottom);
  color:#9a9a9a;font-size:11px}
.f-head{position:absolute;top:40px;color:var(--white);font-size:14px;font-weight:700}
.f-text{position:absolute;color:#a5a5a5;font-size:11px;line-height:25px}
.f-links{position:absolute;top:76px;color:#a5a5a5;font-size:11px;line-height:28px;list-style:none}
</style>
</head>
<body>

<header class="hero" role="img" aria-label="Interior of a recycling plant with conveyor belts and piles of sorted waste">
</header>
<div class="brand"><span class="brand-dot"></span><span class="brand-name">Fernwick 4 Loop</span></div>
<div class="menu-btn"><span style="top:38px"></span><span style="top:45px"></span><span style="top:52px"></span></div>
<h1 class="hero-title center">WE OFFER SUSTAINABLE OPTIONS</h1>
<h2 class="hero-sub center">WITHIN THE WASTE INDUSTRY</h2>
<a class="btn" style="left:375px;top:405px;width:217px;background:var(--red)">Recovery Process</a>
<a class="btn" style="left:608px;top:405px;width:216px;background:var(--green)">Recycling Process</a>
<div class="dots"><i></i><i></i><i></i><i></i></div>

<section>
  <h2 class="abs center intro-title">WE <span class="r">OFFER</span> SUSTAINABLE OPTIONS</h2>
  <p class="abs center intro-sub">WITHIN THE <span class="g">WASTE INDUSTRY</span></p>
  <p class="abs intro-text">Lorem Ipsum is simply dummy text of the printing and typesetting industry. Lorem Ipsum has been the industry's standard dummy text ever since the 1500s, when an unknown printer took a galley of type and scrambled it to make a type specimen book. It has survived not only five centuries, but also the leap into electronic typesetting, remaining essentially unchanged...</p>
</section>

<section>
  <h2 class="abs center section-title" style="top:922px"><span class="r">SERVICES</span> FOR OUR BUSINESS</h2>
  <div class="card" style="left:99px">
    <div class="card-photo" role="img" aria-label="Workers in high-visibility vests wheeling bins" style="background:linear-gradient(160deg,#b9b2a4,#6b7060)"></div>
    <div class="card-label" style="background:var(--blue)"><b>LOREM IPSUM IS SIMPLY</b><em>Click here for view details</em></div>
  </div>
  <div class="card" style="left:352px">
    <div class="card-photo" role="img" aria-label="Row of white collection vans" style="background:linear-gradient(160deg,#d9dde0,#8d9296)"></div>
    <div class="card-label" style="background:var(--rose)"><b>LOREM IPSUM IS SIMPLY</b><em>Click here for view details</em></div>
  </div>
  <div class="card" style="left:605px">
    <div class="card-photo" role="img" aria-label="Assorted recyclable cans and bottles" style="background:linear-gradient(160deg,#c9b48a,#7a6d5c)"></div>
    <div class="card-label" style="background:var(--gold)"><b>LOREM IPSUM IS SIMPLY</b><em>Click here for view details</em></div>
  </div>
  <div class="card" style="left:857px">
    <div class="card-photo" role="img" aria-label="Construction workers on a demolition site" style="background:linear-gradient(160deg,#9a8f86,#5d5a5c)"></div>
    <div class="card-label" style="background:var(--grey)"><b>LOREM IPSUM IS SIMPLY</b><em>Click here for view details</em></div>
  </div>
</section>

<section class="band">
  <p class="band-line"><strong>MARKETS &amp; POLICY</strong>Lorem Ipsum is simply dummy text of the printing and typesetting industry...</p>
  <a class="band-btn">CALL US ANY TIME</a>
</section>

<section class="dev" role="img" aria-label="Faint background of recycling machinery"></section>
<h2 class="abs center section-title" style="top:1589px">OUR <span class="r">DEVELOPMENT</span> PROCESS</h2>
<p class="abs dev-text" style="top:1638px">Lorem Ipsum is simply dummy text of the printing and typesetting industry. Lorem Ipsum has been the industry's standard dummy text ever since the 1500s, when an unknown printer took a galley of type and scrambled it to make a type specimen book...</p>

<svg class="abs" style="left:0;top:1740px" width="1200" height="160" viewBox="0 0 1200 160">
  <polygon points="145,16 372,16 417,76 372,136 145,136" fill="var(--red)"/>
  <polygon points="487,16 714,16 759,76 714,136 487,136" fill="var(--green)"/>
  <polygon points="829,16 1056,16 1101,76 1056,136 829,136" fill="var(--green)"/>
  <g stroke="#fff" stroke-width="6">
    <circle cx="150" cy="76" r="58" fill="var(--red)"/>
    <circle cx="492" cy="76" r="58" fill="var(--green)"/>
    <circle cx="834" cy="76" r="58" fill="var(--green)"/>
  </g>
  <g fill="#fff">
    <circle cx="140" cy="52" r="6"/>
    <rect x="134" y="60" width="12" height="26" rx="3"/>
    <rect x="135" y="86" width="4" height="18"/><rect x="141" y="86" width="4" height="18"/>
    <rect x="152" y="74" width="18" height="3"/>
    <polygon points="153,79 169,79 166,104 156,104"/>
  </g>
  <g fill="#fff">
    <rect x="462" y="62" width="38" height="26" rx="3"/>
    <polygon points="502,68 516,68 524,78 524,88 502,88"/>
    <circle cx="474" cy="92" r="6"/><circle cx="512" cy="92" r="6"/>
  </g>
  <g fill="#fff">
    <rect x="808" y="52" width="9" height="44"/>
    <polygon points="817,96 817,74 833,64 833,74 849,64 849,74 862,66 862,96"/>
  </g>
</svg>
<div class="step-text" style="left:226px;top:1774px"><b>STEP 01</b>Lorem Ipsum is simply dummy text of the printing and typesetting...</div>
<div class="step-text" style="left:568px;top:1774px"><b>STEP 02</b>Lorem Ipsum is simply dummy text of the printing and typesetting...</div>
<div class="step-text" style="left:910px;top:1774px"><b>STEP 03</b>Lorem Ipsum is simply dummy text of the printing and typesetting...</div>

<section>
  <h2 class="abs center section-title" style="top:2079px">WHAT <span class="r">OUR CLIENT'S</span> SAY</h2>
  <p class="abs center" style="top:2126px;font-size:11.5px;color:var(--muted)">Lorem Ipsum is simply dummy text of the printing and typesetting industry. Lorem Ipsum has been the industry...</p>

  <div class="abs" role="img" aria-label="Portrait photo of a client" style="left:100px;top:2202px;width:112px;height:112px;border-radius:50%;background:linear-gradient(160deg,#d9cfc4,#9d8b7c)"></div>
  <span class="mark" style="left:237px;top:2190px">&ldquo;</span>
  <p class="quote" style="left:258px">Lorem Ipsum is simply dummy text of the printing and typesetting industry. Lorem Ipsum has been the industry's standard dummy text ever since...</p>
  <span class="mark" style="left:555px;top:2255px">&rdquo;</span>
  <span class="who" style="left:258px">MARLON KESWICK</span>
  <span class="role" style="left:258px">Business man</span>

  <div class="abs" role="img" aria-label="Portrait photo of a client" style="left:630px;top:2202px;width:112px;height:112px;border-radius:50%;background:linear-gradient(160deg,#d6ccc2,#8e7f74)"></div>
  <span class="mark" style="left:765px;top:2190px">&ldquo;</span>
  <p class="quote" style="left:786px">Lorem Ipsum is simply dummy text of the printing and typesetting industry. Lorem Ipsum has been the industry's standard dummy text ever since...</p>
  <span class="mark" style="left:1083px;top:2255px">&rdquo;</span>
  <span class="who" style="left:786px">MARLON KESWICK</span>
  <span class="role" style="left:786px">Business man</span>

  <div class="abs" style="left:580px;top:2382px;display:flex;gap:7px">
    <i style="width:9px;height:9px;border-radius:50%;background:var(--red)"></i>
    <i style="width:9px;height:9px;border-radius:50%;background:var(--green)"></i>
    <i style="width:9px;height:9px;border-radius:50%;background:var(--green)"></i>
  </div>
</section>

<footer class="footer">
  <div class="abs" style="left:100px;top:118px;width:220px;text-align:center;display:flex;align-items:center;justify-content:center;gap:8px">
    <span style="width:12px;height:12px;border-radius:50%;border:2px solid #8d8d8d"></span>
    <span style="font-family:'Raleway',sans-serif;font-size:19px;font-weight:600;color:#a0a0a0">Fernwick 4 Loop</span>
  </div>

  <h3 class="f-head" style="left:386px">WHO WE ARE?</h3>
  <p class="f-text" style="left:386px;top:76px;width:340px">Lorem Ipsum is simply dummy text of the printing and typesetting industry. Lorem Ipsum has been the industry's standard dummy text ever since the 1500s, when an unknown printer took a galley...</p>
  <p class="f-text" style="left:388px;top:180px;color:var(--white);font-weight:600">Read more info &nbsp;&#10140;</p>

  <h3 class="f-head" style="left:748px">WELCOME</h3>
  <ul class="f-links" style="left:748px">
    <li>Home</li><li>About Us</li><li>Services</li><li>What we do?</li><li>Testimonials</li><li>Contact Us</li>
  </ul>

  <h3 class="f-head" style="left:922px">CONTACT INFO</h3>
  <p class="f-text" style="left:922px;top:76px;width:200px;line-height:21px">120 Street name, City name,<br>Country name : 4120897</p>
  <svg class="abs" style="left:924px;top:131px" width="12" height="12" viewBox="0 0 24 24"><path fill="#a5a5a5" d="M6.6 10.8c1.4 2.8 3.8 5.1 6.6 6.6l2.2-2.2c.3-.3.7-.4 1-.2 1.1.4 2.3.6 3.6.6.6 0 1 .4 1 1V20c0 .6-.4 1-1 1C10.6 21 3 13.4 3 4c0-.6.4-1 1-1h3.5c.6 0 1 .4 1 1 0 1.3.2 2.5.6 3.6.1.3 0 .7-.2 1z"/></svg>
  <p class="f-text" style="left:944px;top:124px">( 4120 ) 338 907</p>
  <svg class="abs" style="left:924px;top:159px" width="12" height="10" viewBox="0 0 24 18"><rect width="24" height="18" rx="2" fill="#a5a5a5"/><path d="M1 2l11 8 11-8" stroke="#2e2e2e" stroke-width="2" fill="none"/></svg>
  <p class="f-text" style="left:944px;top:152px">info@fernwick4loop.com</p>
</footer>
<div class="footer-bottom">
  <span class="abs" style="left:100px;top:24px">© 2015. Fernwick 4 Loop. All rights reserved</span>
  <span class="abs" style="left:772px;top:24px">Connect with our social network :</span>
  <div class="abs" style="left:948px;top:27px;display:flex;gap:20px">
    <i style="width:9px;height:9px;border-radius:50%;background:#8a8a8a"></i>
    <i style="width:9px;height:9px;border-radius:50%;background:#8a8a8a"></i>
    <i style="width:9px;height:9px;border-radius:50%;background:#8a8a8a"></i>
    <i style="width:9px;height:9px;border-radius:50%;background:#8a8a8a"></i>
    <i style="width:9px;height:9px;border-radius:50%;background:#8a8a8a"></i>
  </div>
</div>

</body>
</html>
```